Live Webcasting Host Wants Template/Theme to Jumpstare Ecommerce Site

Please,Please, Please READ ALL OF THE DESCRIPTION. Thank you.

I need a template for a look for my developer to work with in designing an ecommerce site where clients pay a monthly fee for streaming services and video on demand.

I'll need 2 pages designed:
1) public page
2) client log in landing page.

Please use a CMS (WP preferred) as this will allow is for further content to be added after delivery. Please include the pricing text in boxes in slides (pdf) to help fill out you design for the home page.

The attached slides are to give you a general layout of how I envision the pages. Yes I would like the Client page to be tabbed from the side like in the attached slide.

I've attached company logos for use along with the accompanying .psd and .ai files in the zip. Use the colors in logo in site design.

Thank you for your time.
Updates

Please, no designs. This is for a CMS for webpage design like WordPress or Joomla. Thanks. Added Friday, January 13, 2017

Reason: Looking for more designs.

Target Market(s)

Churches, Organizations, Civic Organizations, Government Agencies (State, Local) -BUT don't let this deter your creativity. Decision makers/influencers will be video production and/or IT personnel.

Industry/Entity Type

It Company

Font styles to use
Sans Serif

Colors
f5f5f5
e8e8e8
333333
fece3e
cbcbcb
33a6d7
000000

Requirements
Must have
• Responsive Design
Nice to have
• One Page Design
Should not have
• SHOULD NOT HAVE White overall background but use white in other ways if you like.

```html
<!DOCTYPE html>
<html lang="en">
<head>
<meta charset="utf-8">
<title>Veloca Media — Pricing</title>
<link href="https://fonts.googleapis.com/css2?family=Noto+Sans:wght@400;600;700&display=swap" rel="stylesheet">
<style>
  :root {
    --ink: #333333;
    --ink-soft: #555555;
    --orange: #f89c22;
    --orange-dark: #d77f10;
    --blue: #33a6d7;
    --charcoal: #333333;
    --band: #e8e8e8;
    --page-light: #f5f5f5;
    --page-mid: #cbcbcb;
    --white: #ffffff;
    --black: #000000;
    --social: #9a9a9a;
  }
  * { box-sizing: border-box; margin: 0; padding: 0; }
  html, body { width: 1200px; height: 695px; overflow: hidden; }
  body {
    position: relative;
    font-family: "Noto Sans", Arial, sans-serif;
    color: var(--ink);
    background: radial-gradient(ellipse at 50% 85%, var(--page-light) 0%, #dcdcdc 45%, var(--page-mid) 100%);
  }
  a { text-decoration: none; }

  .site-header {
    position: absolute; left: 0; top: 0; width: 1200px; height: 97px;
    background: var(--white);
    box-shadow: 0 2px 6px rgba(0,0,0,0.12);
  }
  .brand {
    position: absolute; left: 74px; top: 22px;
    font-size: 40px; font-weight: 700; line-height: 44px;
    color: var(--ink); letter-spacing: .5px;
  }
  .main-nav a {
    position: absolute; top: 38px; font-size: 15px; font-weight: 600;
    color: var(--ink); letter-spacing: .2px;
  }
  .login-btn {
    position: absolute; left: 1040px; top: 29px; width: 85px; height: 35px;
    background: var(--orange); color: var(--white); border-radius: 2px;
    font-size: 14px; font-weight: 700; line-height: 35px; text-align: center;
  }

  .plan {
    position: absolute; top: 180px; width: 332px; height: 396px;
    background: var(--white);
    box-shadow: 0 14px 14px -8px rgba(0,0,0,0.28);
  }
  .plan-head {
    height: 54px; background: var(--band); border: 1px solid var(--plan-color);
    border-bottom: none;
  }
  .plan-name {
    position: absolute; left: 20px; top: 16px; font-size: 20px; font-weight: 700;
    color: var(--black); letter-spacing: .3px;
  }
  .plan-price {
    position: absolute; left: 229px; top: -18px; width: 82px; height: 82px;
    border-radius: 50%; background: var(--plan-color); border: 3px solid var(--white);
    box-shadow: 0 0 0 1px rgba(0,0,0,0.06);
    color: var(--white); font-size: 23px; font-weight: 700; text-align: center;
    line-height: 76px;
  }
  .plan-band { position: absolute; left: 0; top: 54px; }
  .plan-icon { position: absolute; left: 28px; top: 90px; }
  .plan-hours {
    position: absolute; left: 92px; top: 88px; width: 212px; color: var(--white);
  }
  .hours-num { display: block; font-size: 28px; font-weight: 700; line-height: 32px; }
  .hours-label { display: block; font-size: 17px; font-weight: 700; line-height: 21px; }
  .hours-note { display: block; font-size: 14.5px; line-height: 19px; margin-top: 3px; }
  .plan-storage {
    position: absolute; left: 92px; top: 244px; width: 200px;
    font-size: 15px; font-weight: 600; line-height: 19px; color: var(--ink-soft);
  }
  .buy-btn {
    position: absolute; left: 93px; top: 315px; width: 165px; height: 48px;
    background: var(--orange); border-radius: 3px;
    box-shadow: 0 3px 0 var(--orange-dark);
    color: var(--white); font-size: 16px; font-weight: 700;
  }
  .buy-label { position: absolute; left: 17px; top: 12px; }
  .buy-arrow {
    position: absolute; right: 0; top: 0; width: 38px; height: 48px;
    background: var(--orange-dark); opacity: .9; border-radius: 0 3px 3px 0;
  }
  .buy-arrow svg { position: absolute; left: 10px; top: 15px; }

  .plan--small  { left: 73px;  --plan-color: var(--orange); }
  .plan--medium { left: 434px; --plan-color: var(--blue); }
  .plan--large  { left: 793px; --plan-color: var(--charcoal); }
  .plan--large .plan-hours { width: 190px; }

  .site-footer {
    position: absolute; left: 0; top: 640px; width: 1200px; height: 55px;
    background: var(--white);
  }
  .legal { position: absolute; left: 79px; top: 16px; font-size: 14px; color: var(--ink-soft); }
  .legal a { color: var(--ink-soft); }
  .legal .sep { margin: 0 9px; color: var(--ink-soft); }
  .social { position: absolute; top: 13px; width: 24px; height: 24px; background: var(--social); }
</style>
</head>
<body>
  <header class="site-header">
    <a class="brand" href="#">Veloca</a>
    <nav class="main-nav">
      <a href="#" style="left:368px">FEATURES</a>
      <a href="#" style="left:471px">PRICING</a>
      <a href="#" style="left:564px">ABOUT US</a>
      <a href="#" style="left:669px">WEBCASTING 101</a>
      <a href="#" style="left:826px">CONTACT</a>
    </nav>
    <a class="login-btn" href="#">LOG IN</a>
  </header>

  <main>
    <article class="plan plan--small">
      <div class="plan-head"></div>
      <h2 class="plan-name">SMALL</h2>
      <svg class="plan-band" width="332" height="180" viewBox="0 0 332 180"><polygon points="0,0 332,0 332,145 0,179" fill="var(--plan-color)"/></svg>
      <div class="plan-price">$49</div>
      <svg class="plan-icon" width="46" height="44" viewBox="0 0 46 44" fill="none" stroke="#fff" stroke-width="2.4"><path d="M30 6H3v30h40V20"/><path d="M8 41h32"/><polygon points="17,14 17,29 29,21.5" fill="#fff" stroke="none"/><circle cx="37" cy="9" r="7" fill="var(--plan-color)"/><path d="M37 5v4h3" stroke-width="1.8"/></svg>
      <div class="plan-hours">
        <span class="hours-num">400</span>
        <span class="hours-label">Viewer Hours</span>
        <span class="hours-note">(50 Viewers watching 2 hrs- 4 times per month)</span>
      </div>
      <p class="plan-storage">100 GB/month of video Storage</p>
      <a class="buy-btn" href="#"><span class="buy-label">Buy Package</span><span class="buy-arrow"><svg width="18" height="16" viewBox="0 0 18 16"><path d="M11 1l6 6-6 6V9C6 9 3 10 1 14 1 8 4 4 11 4z" fill="#fff"/></svg></span></a>
    </article>

    <article class="plan plan--medium">
      <div class="plan-head"></div>
      <h2 class="plan-name">MEDIUM</h2>
      <svg class="plan-band" width="332" height="180" viewBox="0 0 332 180"><polygon points="0,0 332,0 332,145 0,179" fill="var(--plan-color)"/></svg>
      <div class="plan-price">$399</div>
      <svg class="plan-icon" width="46" height="44" viewBox="0 0 46 44" fill="none" stroke="#fff" stroke-width="2.4"><path d="M30 6H3v30h40V20"/><path d="M8 41h32"/><polygon points="17,14 17,29 29,21.5" fill="#fff" stroke="none"/><circle cx="37" cy="9" r="7" fill="var(--plan-color)"/><path d="M37 5v4h3" stroke-width="1.8"/></svg>
      <div class="plan-hours">
        <span class="hours-num">4000</span>
        <span class="hours-label">Viewer Hours</span>
        <span class="hours-note">(500 Viewers watching 2 hrs- 4 times per month)</span>
      </div>
      <p class="plan-storage">500 GB/month of video Storage</p>
      <a class="buy-btn" href="#"><span class="buy-label">Buy Package</span><span class="buy-arrow"><svg width="18" height="16" viewBox="0 0 18 16"><path d="M11 1l6 6-6 6V9C6 9 3 10 1 14 1 8 4 4 11 4z" fill="#fff"/></svg></span></a>
    </article>

    <article class="plan plan--large">
      <div class="plan-head"></div>
      <h2 class="plan-name">LARGE</h2>
      <svg class="plan-band" width="332" height="180" viewBox="0 0 332 180"><polygon points="0,0 332,0 332,145 0,179" fill="var(--plan-color)"/></svg>
      <div class="plan-price">$999</div>
      <svg class="plan-icon" width="46" height="44" viewBox="0 0 46 44" fill="none" stroke="#fff" stroke-width="2.4"><path d="M30 6H3v30h40V20"/><path d="M8 41h32"/><polygon points="17,14 17,29 29,21.5" fill="#fff" stroke="none"/><circle cx="37" cy="9" r="7" fill="var(--plan-color)"/><path d="M37 5v4h3" stroke-width="1.8"/></svg>
      <div class="plan-hours">
        <span class="hours-num">16000</span>
        <span class="hours-label">Viewer Hours</span>
        <span class="hours-note">(2000 Viewers watching 2 hrs- 4 times per month)</span>
      </div>
      <p class="plan-storage">2000 GB/month of video Storage</p>
      <a class="buy-btn" href="#"><span class="buy-label">Buy Package</span><span class="buy-arrow"><svg width="18" height="16" viewBox="0 0 18 16"><path d="M11 1l6 6-6 6V9C6 9 3 10 1 14 1 8 4 4 11 4z" fill="#fff"/></svg></span></a>
    </article>
  </main>

  <footer class="site-footer">
    <p class="legal">© 2017 Veloca Media. All rights reserved<span class="sep">|</span><a href="#">Privacy Policy</a><span class="sep">|</span><a href="#">Terms of Use</a></p>
    <a class="social" href="#" style="left:1048px" aria-label="Social profile"></a>
    <a class="social" href="#" style="left:1074px" aria-label="Social profile"></a>
    <a class="social" href="#" style="left:1100px" aria-label="Social profile"></a>
  </footer>
</body>
</html>
```